Business card for IT company

Looking for a business card for an IT company providing server, network, and application support to medium businesses. Company name is Halvern Systems. Website is www.halvernsystems.example, would like to use the green color that is on the homepage. Prefer design to be done in Illustrator. Please, only DESIGNERS apply - no PHP programmers attempting to do design. Thank you

Industry/Entity Type

Information Technology

Requirements
Must have
• Green
Should not have
• Template designs, or designs done by non-designer type people

```html
<!DOCTYPE html>
<html lang="en">
<head>
<meta charset="utf-8">
<title>Halvern Systems – Business Card</title>
<link rel="stylesheet" href="https://fonts.googleapis.com/css2?family=Exo+2:wght@500&family=Lora:wght@400;700&display=swap">
<style>
  :root {
    --green: #8cc63f;
    --green-light: #a3d55e;
    --orange: #f7941d;
    --sky: #29c1f2;
    --yellow: #fff200;
    --purple: #ab56a5;
    --white: #ffffff;
    --page: #e9e6e1;
  }
  * { box-sizing: border-box; margin: 0; padding: 0; }
  html, body {
    width: 1200px; height: 1200px; overflow: hidden;
    background: var(--page);
  }
  .sheet {
    width: 1200px; height: 1200px;
    display: flex; flex-direction: column; align-items: center; justify-content: center;
    gap: 32px;
  }
  .card {
    width: 920px; height: 526px;
    position: relative; overflow: hidden;
    box-shadow: 0 4px 14px rgba(0,0,0,.15);
  }

  /* Front */
  .card-front {
    background: radial-gradient(ellipse at 55% 35%, var(--green-light) 0%, var(--green) 65%);
  }
  .front-backdrop {
    position: absolute; inset: 0;
    background: linear-gradient(180deg, rgba(255,255,255,0) 45%, rgba(110,170,45,.35) 100%);
  }
  .front-brand {
    position: absolute; left: 0; right: 0; top: 120px;
    display: flex; flex-direction: column; align-items: center;
  }
  .brand-disc {
    width: 150px; height: 150px; border-radius: 50%;
    background: var(--white);
  }
  .brand-name {
    font-family: "Exo 2", sans-serif; font-weight: 500;
    color: var(--white); text-transform: uppercase; text-align: center;
    line-height: 1;
  }
  .front-brand .brand-name { margin-top: 22px; font-size: 54px; letter-spacing: 4px; }
  .brand-sub { display: block; font-size: .5em; letter-spacing: 5px; margin-top: 8px; }
  .brand-rule { width: 220px; height: 2px; background: var(--white); margin-top: 8px; }
  .front-url {
    position: absolute; left: 150px; bottom: 48px;
    font-family: "Exo 2", sans-serif; font-weight: 500; font-size: 20px;
    letter-spacing: 2px; color: var(--white); text-transform: uppercase;
  }

  /* Back */
  .card-back {
    background: var(--green);
    padding: 20px;
    display: grid;
    grid-template-columns: 1fr 1fr 1fr;
    grid-template-rows: 1fr 1.1fr;
    gap: 16px;
  }
  .tile {
    display: flex; flex-direction: column; align-items: center; justify-content: center;
    color: var(--white); font-family: "Lora", serif; text-align: center;
    padding: 18px;
  }
  .tile-brand { background: var(--orange); }
  .tile-brand .brand-disc { width: 90px; height: 90px; }
  .tile-brand .brand-name { margin-top: 12px; font-size: 30px; letter-spacing: 2px; }
  .tile-about {
    grid-column: 2 / 4; background: var(--sky);
    font-size: 27px; line-height: 1.3; padding: 24px 36px;
  }
  .tile-phone { background: var(--yellow); }
  .tile-email { background: var(--purple); }
  .tile-place { background: var(--orange); }
  .tile-icon { width: 60px; height: 60px; margin-bottom: 14px; }
  .tile-phone .contact { font-size: 34px; font-weight: 700; }
  .tile-email .contact, .tile-place .contact { font-size: 21px; font-weight: 700; line-height: 1.3; }
</style>
</head>
<body>
<main class="sheet">
  <section class="card card-front" aria-label="Card front">
    <div class="front-backdrop" role="img" aria-label="Soft green mountain range backdrop"></div>
    <div class="front-brand">
      <div class="brand-disc"></div>
      <p class="brand-name">Halvern<span class="brand-sub">Systems</span></p>
      <div class="brand-rule"></div>
    </div>
    <p class="front-url">http://www.halvernsystems.example</p>
  </section>

  <section class="card card-back" aria-label="Card back">
    <div class="tile tile-brand">
      <div class="brand-disc"></div>
      <p class="brand-name">Halvern<span class="brand-sub">Systems</span></p>
    </div>
    <div class="tile tile-about">
      <p>Supporting clients located in the Northern Los Angeles area. We are reachable around the clock to keep your business running.</p>
    </div>
    <div class="tile tile-phone">
      <svg class="tile-icon" viewBox="0 0 24 24" aria-hidden="true"><path fill="#fff" d="M8.2 2.5c.7-.3 1.4 0 1.7.6l1.4 3c.3.6.1 1.3-.4 1.7l-1.5 1.1c-.3.3-.4.7-.2 1.1.9 2 2.3 3.6 4.3 4.6.4.2.8.1 1.1-.2l1.1-1.5c.4-.5 1.1-.7 1.7-.4l3 1.4c.6.3.9 1 .6 1.7l-.8 2c-.3.8-1.1 1.3-2 1.2C10.6 18.1 5.9 13.4 5.2 5.8c-.1-.9.4-1.7 1.2-2z"/></svg>
      <p class="contact">555.014.2290</p>
    </div>
    <div class="tile tile-email">
      <svg class="tile-icon" viewBox="0 0 24 24" aria-hidden="true"><path fill="#fff" d="M2 5h20v14H2z"/><path fill="none" stroke="#ab56a5" stroke-width="1.6" d="M2.5 5.5L12 13l9.5-7.5"/></svg>
      <p class="contact">support@<br>halvernsystems.example</p>
    </div>
    <div class="tile tile-place">
      <svg class="tile-icon" viewBox="0 0 24 24" aria-hidden="true"><path fill="#fff" d="M12 1.5a7 7 0 0 0-7 7c0 5 7 14 7 14s7-9 7-14a7 7 0 0 0-7-7zm0 4a3 3 0 1 1 0 6 3 3 0 0 1 0-6z"/></svg>
      <p class="contact">Crestmoor Heights, CA</p>
    </div>
  </section>
</main>
</body>
</html>
```